Brenfield Chiropractic Business Cards

[Front]
[KLV/Stormrider LOGO & Brenfield Chiropractic LOGO]
Neck & Back Pain Relief
Dr. Martin Pavely
Doctor of Chiropractic

• Short Term Care For Your Neck & Back Pain
• No Referral Needed
• Affordable / Insurance Accepted
• Proficient in treating Soft Tissue Problems

[Back]
For Valuable Wellness Letter Bulletins™ Emailed To You Free, Go To:
www.DrMartinPavelyJournal.example
[SpinaVault LOGO] - can be small

OFFICE HOURS:
Monday – Thursday
9 am - 12 noon, 2 pm - 6 pm
WALK-INS WELCOME

Industry/Entity Type

Business

Contact Information for Business Card

Brenfield Chiropractic Center, PLLC
4837 Tarrow Avenue, Suite K
Hollisford, NC 28999
(252) 555-0147
www.brenfieldchiro.example

Requirements
Must have
• The KLV/Stormrider Logo
The Brenfield Chiropractic Logo
Should not have
• A picture of a spine

```html
<!DOCTYPE html>
<html lang="en">
<head>
<meta charset="utf-8">
<title>Brenfield Chiropractic Business Cards</title>
<link rel="stylesheet" href="https://fonts.googleapis.com/css2?family=Crimson+Text:wght@400;600;700&display=swap">
<style>
  :root {
    --canvas: #ebe7e1;
    --band-light-top: #f4f5f6;
    --band-light-bottom: #c8d2db;
    --band-purple-edge: #7c6f98;
    --band-purple-core: #5a4c7e;
    --band-blue-top: #3fabd2;
    --band-blue-bottom: #9fdcf0;
    --text-pale: #b9daee;
    --text-dark: #333a44;
    --text-navy: #1f3566;
    --brand-red: #c8242c;
    --brand-blue: #3a63ad;
    --shadow-text: rgba(20, 15, 45, 0.75);
  }
  * { margin: 0; padding: 0; box-sizing: border-box; }
  html, body { width: 1200px; height: 1000px; overflow: hidden; }
  body {
    position: relative;
    background: var(--canvas);
    font-family: "Crimson Text", Georgia, serif;
  }
  .card {
    position: absolute;
    overflow: hidden;
    box-shadow: 4px 6px 10px rgba(0, 0, 0, 0.25);
  }
  .card--front { left: 63px; top: 57px; width: 742px; height: 428px; }
  .card--back { left: 395px; top: 515px; width: 745px; height: 425px; }

  .band { position: absolute; left: 0; right: 0; }
  .band--light { top: 0; height: 136px; background: linear-gradient(var(--band-light-top), var(--band-light-bottom)); }
  .band--purple {
    top: 136px; height: 192px;
    background: linear-gradient(90deg, var(--band-purple-edge), var(--band-purple-core) 50%, var(--band-purple-edge));
    box-shadow: inset 0 6px 8px -4px rgba(0,0,0,0.3), inset 0 -6px 8px -4px rgba(0,0,0,0.3);
  }
  .band--blue { top: 328px; bottom: 0; background: linear-gradient(var(--band-blue-top), var(--band-blue-bottom) 35%, var(--band-blue-bottom)); }
  .card--back .band--purple { height: 190px; }
  .card--back .band--blue { top: 325px; }

  .pale { color: var(--text-pale); text-shadow: 1px 1px 2px var(--shadow-text); }
  .centered { position: absolute; left: 0; right: 0; text-align: center; }

  .brand-name {
    position: absolute; left: 0; right: 0; top: 54px;
    text-align: center;
    font-size: 32px; font-weight: 400; line-height: 36px;
    color: var(--text-dark);
  }

  .doctor { top: 144px; line-height: 1.05; }
  .doctor__name { font-size: 29px; }
  .doctor__title, .doctor__focus { font-size: 24px; }

  .contact {
    position: absolute; left: 27px; top: 252px;
    font-size: 16px; font-weight: 600; line-height: 17px; font-style: normal;
  }
  .contact__line { display: flex; align-items: center; gap: 3px; }
  .contact__line svg { width: 14px; height: 14px; flex: none; }

  .benefits {
    top: 334px; list-style: none;
    font-size: 16px; line-height: 18.5px; color: var(--text-navy);
  }
  .benefits li::before { content: "• "; }

  .partner { position: absolute; font-weight: 700; letter-spacing: 1px; }
  .partner--klv { left: 28px; top: 368px; font-size: 30px; color: var(--brand-red); }
  .partner--stormrider { right: 22px; top: 372px; font-size: 24px; color: var(--text-navy); }

  .network-mark {
    position: absolute; left: 0; right: 0; top: 20px;
    display: flex; justify-content: center; align-items: center; gap: 12px;
    font-size: 46px; font-weight: 700; color: var(--brand-blue);
  }
  .network-mark__square { width: 30px; height: 30px; background: var(--brand-blue); }

  .hours { top: 152px; font-size: 21px; line-height: 24px; }
  .newsletter { top: 276px; font-size: 20px; line-height: 20px; }
  .tm { font-family: Georgia, "Times New Roman", serif; font-size: 0.6em; vertical-align: 0.55em; }
</style>
</head>
<body>

  <section class="card card--front" aria-label="Business card front">
    <div class="band band--light"></div>
    <div class="band band--purple"></div>
    <div class="band band--blue"></div>

    <p class="brand-name">Brenfield Chiropractic</p>

    <div class="centered doctor pale">
      <p class="doctor__name">Dr. Martin Pavely</p>
      <p class="doctor__title">Doctor of Chiropractic</p>
      <p class="doctor__focus">Neck &amp; Back Pain Relief</p>
    </div>

    <address class="contact pale">
      <p>Brenfield Chiropractic Center</p>
      <p class="contact__line">
        <svg viewBox="0 0 14 14" fill="none" stroke="#b9daee" stroke-width="1.3"><path d="M2 7 L7 2.5 L12 7"/><path d="M3.5 6 V12 H10.5 V6"/><path d="M6 12 V9 H8 V12"/></svg>
        PLLC 4837 Tarrow Avenue, Suite K Hollisford, NC 28999
      </p>
      <p class="contact__line">
        <svg viewBox="0 0 14 14" fill="none" stroke="#b9daee" stroke-width="1.2"><circle cx="7" cy="7" r="5.5"/><ellipse cx="7" cy="7" rx="2.4" ry="5.5"/><path d="M1.5 7 H12.5"/></svg>
        www.brenfieldchiro.example
      </p>
      <p class="contact__line">
        <svg viewBox="0 0 14 14" fill="none" stroke="#b9daee" stroke-width="1.2"><rect x="1.5" y="5" width="11" height="7" rx="1.5"/><path d="M2 5 C3 2 11 2 12 5"/><circle cx="7" cy="8.5" r="1.6"/></svg>
        (252) 555-0147
      </p>
    </address>

    <ul class="centered benefits">
      <li>Short Term Care For Your Neck &amp; Back Pain</li>
      <li>No Referral Needed</li>
      <li>Affordable / Insurance Accepted</li>
      <li>Proficient in treating Soft Tissue Problems</li>
    </ul>

    <p class="partner partner--klv">KLV</p>
    <p class="partner partner--stormrider">Stormrider</p>
  </section>

  <section class="card card--back" aria-label="Business card back">
    <div class="band band--light"></div>
    <div class="band band--purple"></div>
    <div class="band band--blue"></div>

    <div class="network-mark"><span class="network-mark__square"></span><span>SpinaVault</span></div>

    <div class="centered hours pale">
      <p>OFFICE HOURS:</p>
      <p>9 am - 12 noon, 2 pm - 6 pm</p>
      <p>Monday – Thursday</p>
      <p>WALK-INS WELCOME</p>
    </div>

    <div class="centered newsletter pale">
      <p>For Valuable Wellness Letter Bulletins<span class="tm">™</span> Emailed To You Free, Go To:</p>
      <p>www.DrMartinPavelyJournal.example</p>
    </div>
  </section>

</body>
</html>
```